Harlan Ridge Smokehouse Jamboree's 10th ever event needs a Poster! This Non-Profit is a blast

We need a totally NEW and FUN poster design to promote our tiny Kentucky town which hosts 40,000+ people who come to meet the TV Celebrity BBQ Pitmasters - who smoke meat for their fans. It is all about Beers, Bands, BBQ + Bourbon. We are a family event with Free music all weekend long.

Target Market(s)

People who love Beer, BBQ, Bands and Bourbon

Colors
ec1f27
0555a3

Requirements
Must have
• Please only use original art.
• High energy / Fresh / Young
• Name: Harlan Ridge Smokehouse Jamboree
• 10th ever
• Sept 4+5, 2020
• Bands, Beer, BBQ + Bourbon
• Hosted by: Copperfield Hollow Distillery
• 2817 Marlow Pike Ashby, KY 40198
• $5 admission - FREE MUSIC - FREE Parking
Nice to have
• Please only use original art. Trademarked images and logos will be rejected.

```html
<!DOCTYPE html>
<html lang="en">
<head>
<meta charset="utf-8">
<title>Harlan Ridge Smokehouse Jamboree – Poster</title>
<link rel="stylesheet" href="https://fonts.googleapis.com/css2?family=Anton&family=Bebas+Neue&family=Kaushan+Script&family=Montserrat:wght@500&display=block">
<style>
  :root {
    --paper: #eceadc;
    --paper-deep: #e2e0cf;
    --red: #e31e36;
    --blue: #5584b4;
    --blue-shadow: #8d93ad;
    --ink: #231f20;
    --gold: #b08f2f;
    --white: #ffffff;
    --pig-pink: #f6dcbc;
    --denim: #7d98b8;
  }
  * { margin: 0; padding: 0; box-sizing: border-box; }
  html, body { width: 856px; height: 1200px; overflow: hidden; background: var(--paper); }
  .poster {
    position: relative;
    width: 856px;
    height: 1200px;
    overflow: hidden;
    background: repeating-linear-gradient(135deg,
      var(--red) 0 34px, var(--paper) 34px 50px,
      var(--blue) 50px 84px, var(--paper) 84px 100px);
  }
  .poster__panel {
    position: absolute;
    left: 33px; top: 25px;
    width: 789px; height: 1142px;
    background: radial-gradient(circle at 50% 45%, var(--paper) 0%, var(--paper-deep) 100%);
  }
  .abs { position: absolute; }
  .center { left: 0; width: 856px; text-align: center; }

  .kicker-rule { top: 78px; left: 55px; width: 746px; height: 20px; }
  .kicker {
    top: 68px;
    font-family: "Bebas Neue", sans-serif;
    font-size: 40px;
    letter-spacing: 5px;
    color: var(--ink);
  }
  .title { top: 100px; left: 0; width: 856px; height: 200px; }
  .edition {
    top: 258px;
    left: 240px; width: 380px; text-align: center;
    font-family: "Kaushan Script", "Yellowtail", cursive;
    font-size: 74px;
    line-height: 1.1;
    color: var(--ink);
    transform: rotate(-6deg);
    text-shadow: 3px 3px 0 var(--white), -3px -3px 0 var(--white), 3px -3px 0 var(--white), -3px 3px 0 var(--white), 6px 6px 0 var(--blue-shadow);
  }
  .mascot {
    top: 385px; left: 248px; width: 374px; height: 315px;
    background: linear-gradient(180deg, var(--pig-pink) 0%, var(--pig-pink) 45%, var(--denim) 75%, var(--paper) 100%);
    border-radius: 48% 48% 8px 8px;
  }
  .chevron { top: 506px; width: 48px; height: 96px; }
  .chevron--left { left: 88px; }
  .chevron--right { left: 724px; }

  .tagline-row { top: 700px; height: 40px; display: flex; align-items: center; justify-content: center; gap: 8px; }
  .tagline {
    font-family: "Bebas Neue", sans-serif;
    font-size: 38px;
    letter-spacing: 1px;
    color: var(--ink);
    line-height: 1;
  }
  .speed-lines { width: 62px; height: 24px; }

  .host-ribbon { top: 744px; left: 114px; width: 628px; height: 62px; }
  .host-ribbon__text {
    top: 754px;
    font-family: "Bebas Neue", sans-serif;
    font-size: 35px;
    letter-spacing: 1px;
    color: var(--white);
    line-height: 42px;
  }

  .info-bracket { top: 842px; width: 8px; height: 172px; }
  .info-block { top: 845px; text-align: center; font-family: "Bebas Neue", sans-serif; color: var(--ink); }
  .info-block--price { left: 126px; width: 150px; }
  .info-block--time { left: 584px; width: 146px; }
  .info-block__big { font-size: 118px; line-height: 100px; }
  .info-block__rule { border-top: 1.5px solid var(--ink); margin: 0 auto; width: 124px; }
  .info-block__small { font-size: 22px; letter-spacing: 1px; line-height: 25px; }
  .info-block__mid { font-size: 32px; letter-spacing: 3px; line-height: 36px; }
  .date-record { top: 820px; left: 324px; width: 210px; height: 210px; }

  .footer-ribbon { top: 1046px; left: 120px; width: 616px; height: 42px; }
  .footer-ribbon__text {
    top: 1046px;
    font-family: "Bebas Neue", sans-serif;
    font-size: 24px;
    letter-spacing: 1.5px;
    line-height: 42px;
    color: var(--white);
  }
  .address {
    top: 1098px;
    font-family: "Bebas Neue", sans-serif;
    font-size: 34px;
    letter-spacing: 4px;
    color: var(--ink);
  }
  .web {
    top: 1137px;
    font-family: "Montserrat", sans-serif;
    font-weight: 500;
    font-size: 15px;
    letter-spacing: 2.6px;
    color: var(--ink);
  }
</style>
</head>
<body>
<main class="poster">
  <div class="poster__panel"></div>

  <svg class="abs kicker-rule" viewBox="0 0 746 20" aria-hidden="true">
    <g stroke="var(--gold)" stroke-width="3" stroke-linecap="round">
      <line x1="0" y1="14" x2="6" y2="14"/><line x1="14" y1="14" x2="82" y2="14"/>
      <line x1="96" y1="14" x2="225" y2="14"/><line x1="58" y1="5" x2="175" y2="5"/>
      <line x1="183" y1="5" x2="225" y2="5"/>
      <line x1="521" y1="14" x2="650" y2="14"/><line x1="664" y1="14" x2="732" y2="14"/>
      <line x1="740" y1="14" x2="746" y2="14"/><line x1="521" y1="5" x2="563" y2="5"/>
      <line x1="571" y1="5" x2="688" y2="5"/>
    </g>
  </svg>
  <div class="abs center kicker">Harlan Ridge</div>

  <svg class="abs title" viewBox="0 0 856 200">
    <g font-family="Anton, sans-serif" font-size="150" text-anchor="middle">
      <text x="434" y="175" textLength="756" lengthAdjust="spacingAndGlyphs" fill="var(--blue-shadow)" stroke="var(--blue-shadow)" stroke-width="10" stroke-linejoin="round">SMOKEHOUSE JAMBOREE</text>
      <text x="428" y="168" textLength="756" lengthAdjust="spacingAndGlyphs" fill="var(--red)" stroke="var(--white)" stroke-width="10" stroke-linejoin="round" paint-order="stroke">SMOKEHOUSE JAMBOREE</text>
    </g>
  </svg>
  <div class="abs edition">10th ever</div>

  <div class="abs mascot" role="img" aria-label="Illustration of a smiling cartoon pig in denim overalls chewing a stalk of grass"></div>

  <svg class="abs chevron chevron--left" viewBox="0 0 48 96" aria-hidden="true">
    <g fill="none" stroke="var(--gold)" stroke-width="2.5">
      <polyline points="44,2 6,44 44,94"/><polyline points="44,16 18,44 44,80"/>
    </g>
  </svg>
  <svg class="abs chevron chevron--right" viewBox="0 0 48 96" aria-hidden="true">
    <g fill="none" stroke="var(--gold)" stroke-width="2.5">
      <polyline points="4,2 42,44 4,94"/><polyline points="4,16 30,44 4,80"/>
    </g>
  </svg>

  <div class="abs center tagline-row">
    <svg class="speed-lines" viewBox="0 0 62 24" aria-hidden="true">
      <g fill="var(--ink)"><polygon points="0,4 62,2 62,5"/><polygon points="8,9 62,8 62,11"/><polygon points="0,14 62,13 62,16"/><polygon points="10,20 62,19 62,22"/></g>
    </svg>
    <span class="tagline">Bands, Beer, BBQ + Bourbon</span>
    <svg class="speed-lines" viewBox="0 0 62 24" aria-hidden="true">
      <g fill="var(--ink)"><polygon points="62,4 0,2 0,5"/><polygon points="54,9 0,8 0,11"/><polygon points="62,14 0,13 0,16"/><polygon points="52,20 0,19 0,22"/></g>
    </svg>
  </div>

  <svg class="abs host-ribbon" viewBox="0 0 628 62" aria-hidden="true">
    <polygon points="0,6 24,6 24,56 0,56 14,31" fill="var(--blue)"/>
    <polygon points="628,6 604,6 604,56 628,56 614,31" fill="var(--blue)"/>
    <rect x="30" y="0" width="568" height="62" fill="var(--blue)"/>
    <rect x="25" y="0" width="2" height="62" fill="var(--blue)"/>
    <rect x="601" y="0" width="2" height="62" fill="var(--blue)"/>
  </svg>
  <div class="abs center host-ribbon__text">Hosted by: Copperfield Hollow Distillery</div>

  <svg class="abs info-bracket" style="left:108px" viewBox="0 0 8 172" aria-hidden="true"><line x1="4" y1="4" x2="4" y2="168" stroke="var(--ink)" stroke-width="2"/><circle cx="4" cy="4" r="4" fill="var(--ink)"/><circle cx="4" cy="168" r="4" fill="var(--ink)"/></svg>
  <svg class="abs info-bracket" style="left:285px" viewBox="0 0 8 172" aria-hidden="true"><line x1="4" y1="4" x2="4" y2="168" stroke="var(--ink)" stroke-width="2"/><circle cx="4" cy="4" r="4" fill="var(--ink)"/><circle cx="4" cy="168" r="4" fill="var(--ink)"/></svg>
  <svg class="abs info-bracket" style="left:563px" viewBox="0 0 8 172" aria-hidden="true"><line x1="4" y1="4" x2="4" y2="168" stroke="var(--ink)" stroke-width="2"/><circle cx="4" cy="4" r="4" fill="var(--ink)"/><circle cx="4" cy="168" r="4" fill="var(--ink)"/></svg>
  <svg class="abs info-bracket" style="left:740px" viewBox="0 0 8 172" aria-hidden="true"><line x1="4" y1="4" x2="4" y2="168" stroke="var(--ink)" stroke-width="2"/><circle cx="4" cy="4" r="4" fill="var(--ink)"/><circle cx="4" cy="168" r="4" fill="var(--ink)"/></svg>

  <div class="abs info-block info-block--price">
    <div class="info-block__big">$5</div>
    <div class="info-block__rule"></div>
    <div class="info-block__small">Single Entry</div>
    <div class="info-block__rule"></div>
    <div class="info-block__mid">Ticket</div>
  </div>

  <svg class="abs date-record" viewBox="0 0 210 210" aria-label="September 4 and 5, 2020">
    <defs><path id="date-arc" d="M 42 105 A 63 63 0 0 1 168 105"/></defs>
    <circle cx="105" cy="105" r="105" fill="var(--ink)"/>
    <circle cx="105" cy="105" r="99" fill="none" stroke="var(--red)" stroke-width="1.5"/>
    <g fill="none" stroke="#3a3637" stroke-width="1">
      <circle cx="105" cy="105" r="52"/><circle cx="105" cy="105" r="57"/><circle cx="105" cy="105" r="62"/>
    </g>
    <circle cx="105" cy="105" r="44" fill="var(--red)"/>
    <circle cx="105" cy="105" r="40" fill="none" stroke="var(--ink)" stroke-width="1"/>
    <text font-family="'Bebas Neue', sans-serif" font-size="28" fill="var(--white)" letter-spacing="1" text-anchor="middle"><textPath href="#date-arc" startOffset="50%">SEPTEMBER</textPath></text>
    <text x="105" y="122" font-family="'Bebas Neue', sans-serif" font-size="50" fill="var(--paper)" text-anchor="middle">4+5</text>
    <text x="105" y="180" font-family="'Bebas Neue', sans-serif" font-size="30" fill="var(--blue)" text-anchor="middle">2020</text>
    <text x="64" y="176" font-size="14" fill="var(--white)" text-anchor="middle">★</text>
    <text x="146" y="176" font-size="14" fill="var(--white)" text-anchor="middle">★</text>
  </svg>

  <div class="abs info-block info-block--time">
    <div class="info-block__big">8PM</div>
    <div class="info-block__rule"></div>
    <div class="info-block__small">Until Midnight</div>
    <div class="info-block__rule"></div>
    <div class="info-block__mid" style="letter-spacing:0">Open Doors</div>
  </div>

  <svg class="abs footer-ribbon" viewBox="0 0 616 42" aria-hidden="true">
    <g stroke="var(--ink)" stroke-width="1.5" stroke-dasharray="6 6">
      <line x1="2" y1="21" x2="148" y2="21"/><line x1="468" y1="21" x2="616" y2="21"/>
    </g>
    <polygon points="154,0 176,0 176,42 154,42 166,21" fill="var(--gold)"/>
    <polygon points="462,0 440,0 440,42 462,42 450,21" fill="var(--gold)"/>
    <rect x="184" y="0" width="248" height="42" fill="var(--gold)"/>
    <rect x="178" y="0" width="2" height="42" fill="var(--gold)"/>
    <rect x="436" y="0" width="2" height="42" fill="var(--gold)"/>
  </svg>
  <div class="abs center footer-ribbon__text">Free Music + Free Parking</div>

  <div class="abs center address">2817 Marlow Pike Ashby, KY 40198</div>
  <div class="abs center web">FOR MORE INFORMATION : WWW.HARLANRIDGEJAMBOREE.COM</div>
</main>
</body>
</html>
```